Mentorvale needs a WordPress - Design

I am a personal, team and business coach and help my clients to develop their potential. I mainly work with individuals and teams, but this can also be in the context of a company.
My business is called "Mentorvale"

The main goal of this website is to promote my business and to attire new customers.
I also want to present my concepts and ideas about coaching and how I actually do coaching and consulting. This is also to inform potential customers what coaching actually is and what it's not.
I want to host this website on a hosting-provider and want to be able to add and adapt content on my own. I'm thus looking for a WordPress - design.

Content:

vision
• Why do I do this
• How do I do this
• What am I doing

Coaching
• Career development
• Conflicts
• What is coaching, why coaching
• Conduct of a session and of the whole consultation
Limits of coaching
• Examples of positive effects of coaching

Support concept

Blog about current topics

Left

About me

Contact form

Footer / disclaimer

The following topics are the most important parts of my daily work as a coach with my clients, maybe this helps to get choos a suitable design:
- personality development, analyzing aspects and patterns and showing their influence
- Improve collaboration and cooperation in teams
- Addressing and solving conflicts (private and business)
- Identify and foster motivation, drivers, goals and action patterns
- Define next steps for the further improvement
- Accompany reorientation in professional career
- Discovering and using the strengths of the customers

The major part of my work is direct conversation with the customer, on site or virtually. My job is to support the customer in recognizing his own ideas, goals and possibilities and to define next steps in the desired direction

Target Market(s)

Small businesses and private persons in serch of a professional coach

Industry/Entity Type

Consultant

Number of Pages Required

1 page

Font styles to use
Sans Serif

Requirements
Must have
• - Logo / Name (see attachment)
- Menu, fixed navigation
- content
- blog
- Footer (contact, disclaimer)

- I need a WordPress design suitable for Mobile and Desktop devices.
- I'm looking for a modern, friendly and easy to use web site.
- First page as Long-pager (scrolling), other pages as long-pager or standard
- Decent, friendly colors but still clear, simple
Nice to have
• - Panorama image (image changing on every load of the site)
- Quote (changing on every load of the site)

```html
<!DOCTYPE html>
<html lang="en">
<head>
<meta charset="utf-8">
<title>Mentorvale – Personal, Team and Business Coaching</title>
<link rel="stylesheet" href="https://fonts.googleapis.com/css2?family=Montserrat:wght@700&family=Poppins:wght@300;400;500;600&display=swap">
<style>
:root{
  --blue:#1ba9e1;
  --blue-deep:#2b4a9e;
  --hero-a:#2d6f9f;
  --hero-b:#3a8fc0;
  --ink:#1d1d1d;
  --text:#4a4a4a;
  --muted:#9a9a9a;
  --soft:#f7f7f7;
  --line:#e3e3e3;
  --white:#ffffff;
}
*{box-sizing:border-box;margin:0;padding:0}
html,body{width:1200px;height:4323px;overflow:hidden}
body{position:relative;background:var(--white);font-family:"Poppins",sans-serif;color:var(--text)}
.abs{position:absolute}
.center{text-align:center}

/* hero */
.hero{left:0;top:0;width:1200px;height:700px;overflow:hidden}
.hero-photo{position:absolute;inset:0;background:linear-gradient(160deg,var(--hero-b) 0%,var(--hero-a) 55%,#3b8bbd 100%)}
.hero-wave{position:absolute;left:0;top:560px;width:1200px;height:140px}
.brand{left:84px;top:28px;display:flex;align-items:center;gap:12px;color:var(--white);font-weight:600;font-size:20px}
.brand-mark{width:30px;height:30px;background:var(--white);opacity:.9}
.topbar{top:26px;left:806px;display:flex;gap:24px;font-size:10px;color:#d8ecf7;align-items:center}
.topbar span{display:flex;align-items:center;gap:6px}
.dots{display:flex;gap:6px}
.dots i{width:14px;height:14px;border:1px solid #d8ecf7;border-radius:50%;display:block}
.nav{top:64px;left:584px;display:flex;gap:20px;font-size:12px;color:#e6f3fa}
.nav a{color:inherit;text-decoration:none}
.hero-title{top:222px;left:0;width:1192px;font-family:"Montserrat",sans-serif;font-weight:700;font-size:82px;color:var(--white);letter-spacing:1px}
.hero-sub{top:346px;left:0;width:1192px;font-size:22px;line-height:31px;color:#eef7fc;font-weight:300}
.share{left:1134px;top:206px;width:66px}
.share div{height:68px;display:flex;align-items:center;justify-content:center;font-size:13px;font-weight:600;color:#1b78b4;background:var(--white);border-bottom:1px solid var(--line)}
.share div:nth-child(2){background:#f0f3f6}

/* vision */
.vision{top:800px;left:0;width:1200px}
.pillar{position:absolute;width:260px;text-align:center}
.pillar svg{display:block;margin:0 auto}
.pillar h3{margin-top:26px;font-size:22px;font-weight:400;color:var(--ink)}
.pillar p{margin-top:14px;font-size:12px;line-height:20px;color:var(--text)}

/* about */
.about{top:1188px;left:0;width:1200px;height:725px;background:var(--soft)}
.about h2{position:absolute;left:118px;top:140px;font-size:40px;font-weight:400;color:var(--ink)}
.about .name{position:absolute;left:118px;top:233px;font-size:20px;color:var(--ink)}
.about .role{position:absolute;left:118px;top:262px;font-size:11px;font-weight:600;color:var(--ink)}
.about .bio{position:absolute;left:118px;top:307px;width:290px;font-size:12px;line-height:20.6px;color:var(--text)}
.about .bio p+p{margin-top:20px}
.pill{position:absolute;display:flex;align-items:center;justify-content:center;border-radius:20px;font-size:12px;font-weight:500;color:var(--white);background:var(--blue)}
.photo-round{position:absolute;border-radius:50%}

/* band */
.band{top:1913px;left:0;width:1200px;height:238px;background:linear-gradient(90deg,#2a8fc4,#2dabd9 60%,#3ab4d9)}
.band h2{position:absolute;top:52px;width:1200px;font-size:44px;font-weight:400;color:var(--white)}
.band p{position:absolute;top:128px;left:270px;width:660px;font-size:12.5px;line-height:20px;font-weight:600;color:var(--white)}

/* coaching */
.coaching h2{position:absolute;left:738px;top:2378px;font-size:44px;font-weight:400;color:var(--ink)}
.topics{position:absolute;left:750px;top:2464px;list-style:none;font-size:12px;color:var(--text)}
.topics li{height:36px;display:flex;align-items:center;gap:9px}
.topics li.sub{padding-left:29px}

/* blog */
.blog{top:2895px;left:0;width:1200px;height:730px;background:var(--soft)}
.blog h2{position:absolute;top:108px;width:1200px;font-size:42px;font-weight:400;color:var(--ink)}
.post{position:absolute;left:395px;top:223px;width:392px;height:392px;border-radius:50%;background:linear-gradient(135deg,#16b4ea 0%,#1e86d0 45%,var(--blue-deep) 100%);color:var(--white);text-align:center}
.post h3{margin-top:84px;font-size:21px;font-weight:400}
.post .meta{margin-top:20px;display:flex;justify-content:center;gap:18px;font-size:12px;font-weight:500}
.post .meta span{display:flex;align-items:center;gap:6px}
.post p{margin:22px auto 0;width:280px;font-size:12px;line-height:20px}
.post .more{display:inline-block;margin-top:22px;width:108px;height:34px;line-height:32px;border:1.5px solid var(--white);border-radius:18px;font-size:12px}

/* contact */
.contact h2{position:absolute;top:3695px;width:1185px;font-size:40px;font-weight:400;color:var(--ink)}
.intro{position:absolute;left:139px;top:3800px;width:380px;font-size:12px;line-height:20px;color:var(--text)}
.field{position:absolute;border:1px solid var(--line);border-radius:18px;background:var(--white);font-size:11px;color:#b5b5b5;padding:0 18px;display:flex;align-items:center}
.field.area{align-items:flex-start;padding-top:10px}
.col-title{position:absolute;font-size:21px;color:var(--ink)}
.info{position:absolute;left:589px;font-size:12px;line-height:20px;color:var(--text);display:flex;gap:12px}
.info svg{flex:none;margin-top:3px}
.links{position:absolute;font-size:12px;line-height:26px;color:var(--text);list-style:none}
.foot-wave{left:0;top:3990px;width:1200px;height:333px}
.copy{left:136px;top:4266px;font-size:11px;color:var(--ink)}
.foot-brand{left:839px;top:4220px;display:flex;align-items:center;gap:16px;font-size:17px;letter-spacing:4px;color:#1f7cc0}
.foot-brand i{width:46px;height:46px;background:#1f4fa3;display:block}
</style>
</head>
<body>

<header class="abs hero">
  <div class="hero-photo" role="img" aria-label="Coach speaking to an audience, blue toned photograph"></div>
  <svg class="hero-wave" viewBox="0 0 1200 140" preserveAspectRatio="none">
    <path d="M0 88 C200 30 420 30 620 70 C820 110 1000 40 1200 128 L1200 140 L0 140 Z" fill="#ffffff"/>
  </svg>
  <div class="abs brand"><span class="brand-mark"></span>Mentorvale</div>
  <div class="abs topbar">
    <span><svg width="11" height="8" viewBox="0 0 11 8"><rect x=".5" y=".5" width="10" height="7" fill="none" stroke="#d8ecf7"/><path d="M.5 .5 5.5 4.5 10.5 .5" fill="none" stroke="#d8ecf7"/></svg>HELLO@MENTORVALE.EXAMPLE</span>
    <span><svg width="10" height="10" viewBox="0 0 10 10"><path d="M2 1 4 3 3 4.5C4 6 5 7 6.5 7L7.5 6 9.5 8 8 9.5C4 9.5 .5 6 .5 2Z" fill="#d8ecf7"/></svg>555 014 7890</span>
    <span class="dots"><i></i><i></i><i></i></span>
  </div>
  <nav class="abs nav">
    <a>HOME</a><a>ABOUT ME</a><a>CHANGE YOUR LIFE</a><a>WORKSHOPS</a><a>SHOP</a><a>BLOG</a><a>CONTACT</a>
  </nav>
  <h1 class="abs hero-title center">Mentorvale</h1>
  <p class="abs hero-sub center">Arthur Penwell, a Latin professor at<br>Ridgefield College</p>
</header>

<aside class="abs share">
  <div>Post</div><div>Chat</div><div>Link</div>
</aside>

<section class="abs vision">
  <div class="pillar" style="left:147px">
    <svg width="86" height="86" viewBox="0 0 86 86"><circle cx="43" cy="43" r="41" fill="none" stroke="#1ba9e1" stroke-width="2"/><circle cx="43" cy="43" r="16" fill="none" stroke="#1ba9e1" stroke-width="2"/><circle cx="43" cy="43" r="6" fill="none" stroke="#1ba9e1" stroke-width="2"/></svg>
    <h3>Why do I do this</h3>
    <p>Arthur Penwell, a Latin<br>professor at Ridgefield<br>College in Virginia</p>
  </div>
  <div class="pillar" style="left:471px">
    <svg width="86" height="86" viewBox="0 0 86 86"><circle cx="43" cy="43" r="41" fill="none" stroke="#1ba9e1" stroke-width="2"/><circle cx="35" cy="40" r="7" fill="none" stroke="#1ba9e1" stroke-width="2"/><circle cx="51" cy="40" r="7" fill="none" stroke="#1ba9e1" stroke-width="2"/><path d="M26 58c3-6 15-6 17 0M43 58c3-6 15-6 17 0" fill="none" stroke="#1ba9e1" stroke-width="2"/></svg>
    <h3>How do I do this</h3>
    <p>Arthur Penwell, a Latin<br>professor at Ridgefield<br>College in Virginia</p>
  </div>
  <div class="pillar" style="left:790px">
    <svg width="86" height="86" viewBox="0 0 86 86"><circle cx="43" cy="43" r="41" fill="none" stroke="#1ba9e1" stroke-width="2"/><circle cx="43" cy="43" r="12" fill="none" stroke="#1ba9e1" stroke-width="2"/><path d="M43 23v8M43 55v8M23 43h8M55 43h8" stroke="#1ba9e1" stroke-width="2"/></svg>
    <h3>What am I doing</h3>
    <p>Arthur Penwell, a Latin<br>professor at Ridgefield<br>College in Virginia</p>
  </div>
</section>

<section class="abs about">
  <h2>About Me</h2>
  <div class="name">Jane Doe</div>
  <div class="role">A personal mentor</div>
  <div class="bio">
    <p>Arthur Penwell, a Latin professor at Ridgefield College in Virginia oked up one of the more obscure Latin words, consectetur, from a Lorem Ipsum passage, and going through the cites of the word in classical literature, discovered the</p>
    <p>undoubtable source. Lorem Ipsum comes from sections 1.10.32 and 1.10.33 of</p>
  </div>
  <a class="pill" style="left:121px;top:522px;width:107px;height:34px">View More</a>
  <div class="photo-round" style="left:538px;top:87px;width:538px;height:538px;background:radial-gradient(circle,#f2f2f2,#dedede)" role="img" aria-label="Group of students seated in a circle with notebooks, seen from above"></div>
</section>

<section class="abs band">
  <h2 class="center">Examples of positive effects of coaching</h2>
  <p class="center">Arthur Penwell, a Latin professor at Ridgefield College in Virginia oked up one of the more obscure Latin words, consectetur, from a Lorem Ipsum passage</p>
</section>

<section class="coaching">
  <div class="photo-round" style="left:120px;top:2246px;width:536px;height:536px;background:linear-gradient(135deg,#eef3f4,#cfd8dc 60%,#3b5a7a)" role="img" aria-label="Coach with a tablet answering a raised hand in a bright classroom"></div>
  <h2>Coaching</h2>
  <ul class="topics">
    <li><svg width="14" height="14" viewBox="0 0 14 14"><circle cx="7" cy="7" r="6" fill="none" stroke="#1ba9e1" stroke-width="1.4"/><path d="M4 7.2 6.2 9.2 10 5" fill="none" stroke="#1ba9e1" stroke-width="1.4"/></svg>Career development</li>
    <li><svg width="14" height="14" viewBox="0 0 14 14"><circle cx="7" cy="7" r="6" fill="none" stroke="#1ba9e1" stroke-width="1.4"/><path d="M4 7.2 6.2 9.2 10 5" fill="none" stroke="#1ba9e1" stroke-width="1.4"/></svg>Conflicts</li>
    <li><svg width="14" height="14" viewBox="0 0 14 14"><circle cx="7" cy="7" r="6" fill="none" stroke="#1ba9e1" stroke-width="1.4"/><path d="M4 7.2 6.2 9.2 10 5" fill="none" stroke="#1ba9e1" stroke-width="1.4"/></svg>What is coaching, why coaching</li>
    <li><svg width="14" height="14" viewBox="0 0 14 14"><circle cx="7" cy="7" r="6" fill="none" stroke="#1ba9e1" stroke-width="1.4"/><path d="M4 7.2 6.2 9.2 10 5" fill="none" stroke="#1ba9e1" stroke-width="1.4"/></svg>Conduct of a session and of the whole consultation</li>
    <li class="sub">Limits of coaching</li>
    <li><svg width="14" height="14" viewBox="0 0 14 14"><circle cx="7" cy="7" r="6" fill="none" stroke="#1ba9e1" stroke-width="1.4"/><path d="M4 7.2 6.2 9.2 10 5" fill="none" stroke="#1ba9e1" stroke-width="1.4"/></svg>Examples of positive effects of coaching</li>
  </ul>
</section>

<section class="abs blog">
  <h2 class="center">Blog about current topics</h2>
  <div class="photo-round" style="left:129px;top:276px;width:286px;height:286px;background:linear-gradient(135deg,#f3efe9,#d9c7a8)" role="img" aria-label="Woman holding a red clipboard, thinking"></div>
  <div class="photo-round" style="left:763px;top:276px;width:286px;height:286px;background:linear-gradient(135deg,#eef2f3,#c9d3d8)" role="img" aria-label="Coach standing in front of a seated group"></div>
  <article class="post">
    <h3>Vivamus porta</h3>
    <div class="meta">
      <span><svg width="16" height="16" viewBox="0 0 16 16"><circle cx="8" cy="8" r="7" fill="none" stroke="#fff" stroke-width="1.3"/><circle cx="8" cy="6.5" r="2.5" fill="none" stroke="#fff" stroke-width="1.3"/><path d="M3.5 13c1.5-3 7.5-3 9 0" fill="none" stroke="#fff" stroke-width="1.3"/></svg>admin</span>
      <span><svg width="16" height="16" viewBox="0 0 16 16"><rect x="1.5" y="3" width="13" height="11.5" fill="none" stroke="#fff" stroke-width="1.3"/><path d="M1.5 6.5h13M5 1.5v3M11 1.5v3" stroke="#fff" stroke-width="1.3"/></svg>08/03/2016</span>
    </div>
    <p>Arthur Penwell, a Latin professor at Ridgefield College in Virginia ne of the more obscure Latin words</p>
    <a class="more">View More</a>
  </article>
</section>

<svg class="abs foot-wave" viewBox="0 0 1200 333" preserveAspectRatio="none">
  <path d="M0 190 C260 120 520 200 760 140 C940 95 1080 40 1200 60 L1200 333 L0 333 Z" fill="#f4f4f4"/>
  <path d="M0 230 C300 170 560 250 820 190 C980 150 1100 120 1200 130 L1200 333 L0 333 Z" fill="#ececec"/>
  <path d="M0 270 C320 220 600 290 880 240 C1020 215 1120 200 1200 205 L1200 333 L0 333 Z" fill="#ffffff"/>
</svg>

<section class="contact">
  <h2 class="center">Contact Us</h2>
  <p class="intro">Arthur Penwell, a Latin professor at Ridgefield<br>College in Virginia oked up one of the</p>
  <div class="field" style="left:133px;top:3866px;width:176px;height:36px">Your Name...</div>
  <div class="field" style="left:322px;top:3866px;width:181px;height:36px">Your Email...</div>
  <div class="field" style="left:134px;top:3923px;width:369px;height:37px">Your Phone...</div>
  <div class="field area" style="left:133px;top:3979px;width:370px;height:66px">Message...</div>
  <a class="pill" style="left:134px;top:4067px;width:151px;height:35px">Send Message</a>

  <div class="col-title" style="left:582px;top:3794px">Mentorvale</div>
  <div class="info" style="top:3860px"><svg width="12" height="12" viewBox="0 0 10 10"><path d="M2 1 4 3 3 4.5C4 6 5 7 6.5 7L7.5 6 9.5 8 8 9.5C4 9.5 .5 6 .5 2Z" fill="#1ba9e1"/></svg>+00 555 014 789</div>
  <div class="info" style="top:3901px"><svg width="12" height="9" viewBox="0 0 11 8"><rect width="11" height="8" fill="#1ba9e1"/><path d="M0 0 5.5 4.5 11 0" fill="none" stroke="#fff"/></svg>hello@mentorvale.example</div>
  <div class="info" style="top:3942px"><svg width="12" height="15" viewBox="0 0 12 15"><path d="M6 0a6 6 0 0 1 6 6c0 4-6 9-6 9S0 10 0 6a6 6 0 0 1 6-6z" fill="#1ba9e1"/><circle cx="6" cy="6" r="2.2" fill="#fff"/></svg>PO Box 41208 Elm st. 212, Fairhaven,<br>California, US.</div>

  <div class="col-title" style="left:878px;top:3791px">Links</div>
  <ul class="links" style="left:878px;top:3851px"><li>About me</li><li>FAQs</li><li>Contact</li><li>Clients</li><li>News</li></ul>
  <ul class="links" style="left:999px;top:3851px"><li>Success Stories</li><li>Shop</li><li>Privacy policy</li></ul>
</section>

<footer>
  <div class="abs copy">Copyright © 2020 Mentorvale.</div>
  <div class="abs foot-brand"><i></i>MENTORVALE</div>
</footer>

</body>
</html>
```